Tamsel Loans - Mortgage Brokers Australia

redesign of tamselloans.com.au website. We are a mortgage brokering service and are clients are based in Australia. The demographics are 30-45 year holds looking to borrow money to purchase, invest and refinance property.

Please research other lending websites in Australia. My favourites are:

https://www.korvu.com.au/
https://www.brivanest.com.au/

I want CTA's on the first page. For Refinance/Purchase.

I DO NOT WANT ANYONE TO TRY AND CONTACT ME VIA EMAIL/What's app

My current website is: https/www.tamselloans.com.au/home and the password is "Rbqw8175?"

Target Market(s)

30-45 year hold professionals, first home buyers

Industry/Entity Type

Mortgage Brokerage

Number of Pages Required

4 page

Font styles to use
Sans Serif

Colors
e34197
6b449b
ffc214
0792cd
34a7d8

Requirements
Must have
• Must be fresh, clean and professional - with a beautiful hero section

```html
<!DOCTYPE html>
<html lang="en">
<head>
<meta charset="utf-8">
<title>Tamsel Loans – Mortgage Brokers Australia</title>
<link rel="stylesheet" href="https://fonts.googleapis.com/css2?family=Baloo+2:wght@500;600;700&family=Poppins:wght@400;500;600&display=swap">
<style>
:root{
  --pink:#e34197;
  --purple:#6b449b;
  --yellow:#f6c31a;
  --ink:#2b2b2b;
  --grey:#666;
  --black:#050505;
  --bar:#3a3a3a;
  --white:#fff;
}
*{box-sizing:border-box;margin:0;padding:0}
html,body{width:1200px;height:5101px;overflow:hidden}
body{position:relative;background:var(--white);font-family:"Poppins",sans-serif;color:var(--ink)}
.abs{position:absolute}
.btn{position:absolute;display:flex;align-items:center;justify-content:center;border-radius:30px;color:#fff;font-weight:600;font-size:15px;text-transform:uppercase;letter-spacing:.3px;box-shadow:0 4px 8px rgba(0,0,0,.18)}
.btn.pink{background:var(--pink)}
.btn.purple{background:var(--purple)}
.section-title{position:absolute;left:0;width:1200px;text-align:center;font-family:"Baloo 2",sans-serif;font-weight:600;font-size:38px;color:var(--purple)}

/* header */
.brand{left:172px;top:60px;font-family:"Baloo 2",sans-serif;font-weight:600;font-size:40px;color:var(--pink);line-height:1}
.socials{left:650px;top:25px;display:flex;gap:9px}
.socials span{width:30px;height:30px;border-radius:50%;background:#f2993a}
.contact-top{left:832px;top:16px;display:flex;gap:12px;align-items:center}
.contact-top small{display:block;font-size:13px;font-weight:600;color:var(--ink)}
.contact-top strong{display:block;font-size:23px;font-weight:500;color:var(--pink);line-height:1.1}
.nav{left:414px;top:80px;width:786px;height:60px;background:var(--yellow);clip-path:polygon(58px 0,100% 0,100% 100%,0 100%)}
.nav-home{left:414px;top:80px;width:112px;height:60px;background:var(--pink);clip-path:polygon(58px 0,100% 0,100% 100%,0 100%)}
.nav-links{position:absolute;left:476px;top:80px;height:60px;display:flex;align-items:center;gap:20px;font-size:14px;font-weight:500;color:#fff;list-style:none}

/* hero */
.hero-photo{left:0;top:140px;width:1200px;height:640px;background:linear-gradient(90deg,#f4f4f4 0%,#eaeef3 35%,#a9bcd1 60%,#d7c3b4 80%,#efe7e0 100%)}
.hero-title{left:172px;top:212px;font-family:"Baloo 2",sans-serif;font-weight:600;font-size:40px;line-height:48px;color:var(--ink)}
.hero-title em{font-style:normal;color:var(--pink)}

/* advice */
.advice{left:0;top:680px;width:1200px;height:534px;background:var(--yellow);clip-path:polygon(0 92px,600px 0,100% 92px,100% 100%,0 100%)}
.advice-title{left:0;top:766px;width:1200px;text-align:center;font-family:"Baloo 2",sans-serif;font-weight:600;font-size:33px;color:#fff}
.advice-card{top:866px;width:266px;height:266px;background:#fff;border-radius:4px;box-shadow:0 3px 10px rgba(0,0,0,.15);text-align:center}
.advice-card svg{position:absolute;left:103px;top:22px}
.advice-card h3{position:absolute;top:96px;left:0;width:100%;font-family:"Baloo 2",sans-serif;font-weight:500;font-size:25px;line-height:32px;color:var(--ink)}
.advice-card .btn{left:70px;top:186px;width:126px;height:46px;font-size:13px}

/* lenders */
.lender{top:1382px;width:156px;height:92px;background:#fff;border-radius:4px;box-shadow:0 2px 8px rgba(0,0,0,.13);display:flex;align-items:center;justify-content:center;font-family:"Baloo 2",sans-serif;font-weight:700;font-size:22px}

/* services */
.service{top:1667px;width:202px;height:270px;background:#fff;box-shadow:0 2px 8px rgba(0,0,0,.14);text-align:center}
.service .band{position:absolute;left:0;top:0;width:202px;height:136px;clip-path:polygon(0 0,100% 0,100% 100%,50% 78%,0 100%)}
.service svg{position:absolute;left:68px;top:22px}
.service h3{position:absolute;top:153px;left:0;width:100%;font-size:16px;font-weight:500}
.service p{position:absolute;top:184px;left:8px;width:186px;font-size:11px;line-height:21px;color:var(--grey)}
.purple-band{background:var(--purple)}
.pink-band{background:var(--pink)}
.purple-text{color:var(--purple)}
.pink-text{color:var(--pink)}

/* assess */
.assess{left:0;top:2050px;width:1200px;height:630px;background:linear-gradient(90deg,#f3f5f9 0%,#eef1f6 45%,#cfd4dd 65%,#b9a48f 80%,#8b97a8 100%);clip-path:polygon(0 80px,600px 0,100% 80px,100% 100%,0 100%)}
.assess-title{left:172px;top:2182px;font-family:"Baloo 2",sans-serif;font-weight:600;font-size:40px;line-height:46px;color:var(--purple)}
.checklist{left:172px;top:2345px;list-style:none;font-size:14px;font-weight:500;line-height:33px;color:var(--ink)}
.checklist li{display:flex;align-items:center;gap:10px}

/* how */
.how-photo{left:0;top:2742px;width:640px;height:470px;background:linear-gradient(90deg,#7a8290 0%,#c5c8ce 40%,#e9e5e0 70%,#fff 100%)}
.how-title{left:600px;top:2760px;font-family:"Baloo 2",sans-serif;font-weight:600;font-size:38px;color:var(--purple)}
.how-text{left:600px;top:2832px;width:430px;font-size:11.6px;line-height:25.5px;color:var(--ink)}

/* difference */
.difference{left:0;top:3128px;width:1200px;height:500px;background:var(--purple);clip-path:polygon(0 80px,600px 0,100% 80px,100% 100%,0 100%)}
.diff-title{left:0;top:3246px;width:1200px;text-align:center;font-family:"Baloo 2",sans-serif;font-weight:500;font-size:38px;line-height:46px;color:#fff}
.diff-text{left:0;top:3372px;width:1200px;text-align:center;font-size:17.5px;line-height:36px;color:#fff}

/* blog */
.post{top:3802px;width:266px;height:460px;background:#fff;box-shadow:0 2px 8px rgba(0,0,0,.14);text-align:center}
.post .thumb{position:absolute;left:0;top:0;width:266px;height:170px;background:linear-gradient(160deg,#9aa5b3,#d9dde2 55%,#7d8694)}
.post .thumb::after{content:"";position:absolute;left:0;bottom:0;width:100%;height:26px;background:#fff;clip-path:polygon(0 100%,50% 0,100% 100%)}
.post h3{position:absolute;top:186px;left:20px;width:226px;font-size:16px;font-weight:500;line-height:25px}
.post p{position:absolute;top:272px;left:14px;width:238px;font-size:11px;line-height:21px;color:var(--grey)}
.post .btn{left:83px;top:400px;width:100px;height:42px;font-size:12px}

/* footer */
.footer{left:0;top:4326px;width:1200px;height:698px;background:var(--black);clip-path:polygon(0 0,600px 90px,100% 0,100% 100%,0 100%)}
.footer-title{top:4512px;font-family:"Baloo 2",sans-serif;font-weight:500;font-size:38px;color:#fff}
.field{position:absolute;background:#fff;border-radius:28px;font-size:12px;padding:0 18px;display:flex;align-items:center;color:var(--ink)}
.submit{left:172px;top:4886px;width:142px;height:56px;background:var(--yellow);font-size:16px}
.contact-intro{left:681px;top:4584px;width:350px;font-size:12.5px;line-height:25px;color:#fff}
.contact-item{left:681px;display:flex;gap:20px;align-items:center;color:#fff;font-size:12.5px;line-height:20px}
.contact-item .icon{width:46px;height:46px;border-radius:50%;background:var(--yellow);display:flex;align-items:center;justify-content:center;flex:none}
.copyright{left:0;top:5024px;width:1200px;height:77px;background:var(--bar);display:flex;align-items:center;justify-content:center;color:#fff;font-size:12.5px}
</style>
</head>
<body>

<!-- Header -->
<div class="abs brand">Tamsel Loans</div>
<div class="abs socials"><span></span><span></span><span></span><span></span></div>
<div class="abs contact-top">
  <svg width="22" height="40" viewBox="0 0 22 40"><rect x="2" y="2" width="18" height="36" rx="3" fill="none" stroke="#e34197" stroke-width="3"/><circle cx="11" cy="32" r="2" fill="#e34197"/></svg>
  <div><small>CONTACT US</small><strong>(02) 5550 1847</strong></div>
</div>
<div class="abs nav"></div>
<div class="abs nav-home"></div>
<ul class="nav-links"><li>HOME</li><li>OUR SERVICES</li><li>ABOUT US</li><li>WHY USE BROKER</li><li>BLOG</li><li>CONTACT</li></ul>

<!-- Hero -->
<div class="abs hero-photo" role="img" aria-label="Photo of a smiling couple reviewing loan documents with a broker at a laptop"></div>
<h1 class="abs hero-title">We are <em>PASSIONATE</em> about helping<br><em>YOU</em> achieve your<br>financial goals!</h1>
<div class="btn pink" style="left:172px;top:394px;width:150px;height:56px;">Get a quote</div>

<!-- Free advice -->
<div class="abs advice"></div>
<h2 class="abs advice-title">Your Free Advice Starts Here</h2>

<div class="abs advice-card" style="left:172px">
  <svg width="60" height="60" viewBox="0 0 60 60" fill="none" stroke="#222" stroke-width="2.5"><path d="M6 28 30 6l24 22"/><path d="M12 24v30h36V24"/><text x="30" y="46" text-anchor="middle" font-size="22" fill="#222" stroke="none" font-family="Poppins,sans-serif">$</text></svg>
  <h3>I want to buy<br>a home</h3>
  <div class="btn pink">Get started</div>
</div>
<div class="abs advice-card" style="left:467px">
  <svg width="60" height="60" viewBox="0 0 60 60" fill="none" stroke="#222" stroke-width="2.5"><circle cx="30" cy="13" r="10"/><text x="30" y="19" text-anchor="middle" font-size="15" fill="#222" stroke="none" font-family="Poppins,sans-serif">$</text><path d="M4 36l12-8 14 8 14-8 12 8"/><path d="M16 28l10 20h8l10-20"/></svg>
  <h3>I want to<br>Refinance</h3>
  <div class="btn pink">Get started</div>
</div>
<div class="abs advice-card" style="left:762px">
  <svg width="60" height="60" viewBox="0 0 60 60" fill="none" stroke="#222" stroke-width="2.5"><circle cx="30" cy="12" r="9"/><text x="30" y="17" text-anchor="middle" font-size="13" fill="#222" stroke="none" font-family="Poppins,sans-serif">$</text><path d="M6 32l24-10 24 10"/><rect x="10" y="32" width="40" height="22"/><rect x="18" y="38" width="8" height="8"/><rect x="34" y="38" width="8" height="8"/></svg>
  <h3>I want to buy an<br>Investment</h3>
  <div class="btn pink">Get started</div>
</div>

<!-- Lenders -->
<h2 class="section-title" style="top:1284px">Our Lenders</h2>
<div class="abs lender" style="left:172px;color:#d8262e">Calder Money</div>
<div class="abs lender" style="left:347px;color:#0a4b8c">Norvane</div>
<div class="abs lender" style="left:521px;color:#333">Westlark</div>
<div class="abs lender" style="left:695px;color:#1a2c6b">Orbisa</div>
<div class="abs lender" style="left:870px;color:#d8262e">Calder Money</div>

<!-- Services -->
<h2 class="section-title" style="top:1562px">Our Services</h2>
<div class="abs service" style="left:172px">
  <div class="band purple-band"></div>
  <svg width="66" height="66" viewBox="0 0 66 66" fill="none" stroke="#fff" stroke-width="2.5"><path d="M4 30 24 12l20 18"/><path d="M10 26v30h22"/><circle cx="46" cy="46" r="14"/><text x="46" y="52" text-anchor="middle" font-size="17" fill="#fff" stroke="none" font-family="Poppins,sans-serif">$</text></svg>
  <h3 class="purple-text">HOME LOANS</h3>
  <p>Tamsel Loans manage the entire process for you from start to finish</p>
</div>
<div class="abs service" style="left:390px">
  <div class="band pink-band"></div>
  <svg width="66" height="66" viewBox="0 0 66 66" fill="none" stroke="#fff" stroke-width="2.5"><path d="M4 28 28 8l24 20"/><path d="M10 24v30h20"/><text x="28" y="44" text-anchor="middle" font-size="20" fill="#fff" stroke="none" font-family="Poppins,sans-serif">$</text><rect x="36" y="34" width="22" height="26"/><path d="M41 42h12M41 48h12M41 54h8"/></svg>
  <h3 class="pink-text">PERSONAL LOANS</h3>
  <p>Tamsel Loans manage the entire process for you from start to finish</p>
</div>
<div class="abs service" style="left:608px">
  <div class="band purple-band"></div>
  <svg width="66" height="66" viewBox="0 0 66 66" fill="none" stroke="#fff" stroke-width="2.5"><circle cx="18" cy="14" r="10"/><text x="18" y="20" text-anchor="middle" font-size="14" fill="#fff" stroke="none" font-family="Poppins,sans-serif">$</text><path d="M12 36l6-12h30l6 12"/><rect x="8" y="36" width="50" height="14" rx="3"/><circle cx="18" cy="54" r="5"/><circle cx="48" cy="54" r="5"/></svg>
  <h3 class="purple-text">CAR LOANS</h3>
  <p>Tamsel Loans manage the entire process for you from start to finish</p>
</div>
<div class="abs service" style="left:826px">
  <div class="band pink-band"></div>
  <svg width="66" height="66" viewBox="0 0 66 66" fill="none" stroke="#fff" stroke-width="2.5"><path d="M6 18 33 6l27 12z"/><path d="M10 22h46M12 26v26M54 26v26M10 56h46M6 60h54"/><rect x="22" y="28" width="22" height="22"/><text x="33" y="45" text-anchor="middle" font-size="16" fill="#fff" stroke="none" font-family="Poppins,sans-serif">$</text></svg>
  <h3 class="pink-text">INVESTMENT LOANS</h3>
  <p>Tamsel Loans manage the entire process for you from start to finish</p>
</div>

<!-- Assess -->
<div class="abs assess" role="img" aria-label="Photo of a couple signing mortgage papers with a broker at an office desk"></div>
<h2 class="abs assess-title">We assess &amp; tailor your<br>mortgage to suit your financial<br>situation</h2>
<ul class="abs checklist">
  <li><svg width="14" height="14" viewBox="0 0 14 14" fill="none" stroke="#333" stroke-width="1.6"><path d="M2 7l3 3 7-7"/></svg>We listen to you and learn</li>
  <li><svg width="14" height="14" viewBox="0 0 14 14" fill="none" stroke="#333" stroke-width="1.6"><path d="M2 7l3 3 7-7"/></svg>We create breathing space for you</li>
  <li><svg width="14" height="14" viewBox="0 0 14 14" fill="none" stroke="#333" stroke-width="1.6"><path d="M2 7l3 3 7-7"/></svg>We develop your Mortgage plan</li>
  <li><svg width="14" height="14" viewBox="0 0 14 14" fill="none" stroke="#333" stroke-width="1.6"><path d="M2 7l3 3 7-7"/></svg>We select the right financial institution</li>
  <li><svg width="14" height="14" viewBox="0 0 14 14" fill="none" stroke="#333" stroke-width="1.6"><path d="M2 7l3 3 7-7"/></svg>We help build your secure future</li>
</ul>
<div class="btn pink" style="left:198px;top:2528px;width:128px;height:50px;font-size:14px;">Book now</div>

<!-- How we work -->
<div class="abs how-photo" role="img" aria-label="Photo of a family meeting with a broker to go over loan options"></div>
<h2 class="abs how-title">How We Work With You</h2>
<p class="abs how-text">Tamsel Loans manage the entire process for you from start to finish and as every one of our clients is different, we fully assess your individual situation and provide a solution to meet your particular needs. Quite simply, we do everything necessary to get you the best possible rate and importantly get your loan over the line.</p>
<div class="btn pink" style="left:600px;top:2988px;width:128px;height:50px;font-size:14px;">Book now</div>

<!-- Difference -->
<div class="abs difference"></div>
<h2 class="abs diff-title">Give Us A Chance To Make<br>A Difference!</h2>
<p class="abs diff-text">We’re all about helping you reach your next financial goal—great rates, less fees,<br>unprecedented service, and awesome loan help.</p>
<div class="btn pink" style="left:518px;top:3480px;width:164px;height:56px;font-size:15px;">Book in now</div>

<!-- Blog -->
<h2 class="section-title" style="top:3704px">Blog Posts</h2>
<div class="abs post" style="left:172px">
  <div class="thumb" role="img" aria-label="Photo of business owners talking in an office"></div>
  <h3>Flow of credit to small businesses remains strong</h3>
  <p>Small business owners in need of credit will be buoyed by new data that shows the approval rate for loans has remained strong throughout the coronavirus crisis.</p>
  <div class="btn pink">Read more</div>
</div>
<div class="abs post" style="left:467px">
  <div class="thumb" role="img" aria-label="Photo of a smiling family at home"></div>
  <h3>WageBridge 2.0 is about to begin: here’s what you need to know</h3>
  <p>Small business owners in need of credit will be buoyed by new data that shows the approval rate for loans has remained strong throughout the coronavirus crisis.</p>
  <div class="btn purple">Read more</div>
</div>
<div class="abs post" style="left:762px">
  <div class="thumb" role="img" aria-label="Photo of investors in a modern office"></div>
  <h3>Is now a good time to buy property? Two-thirds of investors say ‘yes’</h3>
  <p>Small business owners in need of credit will be buoyed by new data that shows the approval rate for loans has remained strong throughout the coronavirus crisis.</p>
  <div class="btn pink">Read more</div>
</div>

<!-- Footer -->
<div class="abs footer"></div>
<h2 class="abs footer-title" style="left:172px">Contact Form</h2>
<div class="field" style="left:172px;top:4588px;width:216px;height:54px">First Name</div>
<div class="field" style="left:398px;top:4588px;width:216px;height:54px">Last Name</div>
<div class="field" style="left:172px;top:4662px;width:216px;height:54px">Email</div>
<div class="field" style="left:398px;top:4662px;width:216px;height:54px">Phone</div>
<div class="field" style="left:172px;top:4736px;width:442px;height:132px;align-items:flex-start;padding-top:16px;border-radius:30px">Message</div>
<div class="btn submit">Submit</div>

<h2 class="abs footer-title" style="left:681px">Contact Us</h2>
<p class="abs contact-intro">Call or email us, or if you have any questions, queries, or enquiries please leave the form and we will be in contact with you.</p>
<div class="abs contact-item" style="top:4664px">
  <div class="icon"><svg width="22" height="24" viewBox="0 0 22 24" fill="none" stroke="#111" stroke-width="2"><path d="M11 22s8-8 8-13a8 8 0 0 0-16 0c0 5 8 13 8 13z"/><circle cx="11" cy="9" r="3"/></svg></div>
  <div>14 Harlow Street<br>Larkvale, NSW 2199 Australia</div>
</div>
<div class="abs contact-item" style="top:4732px">
  <div class="icon"><svg width="22" height="22" viewBox="0 0 22 22" fill="none" stroke="#111" stroke-width="2"><path d="M4 2h4l2 5-3 2a12 12 0 0 0 6 6l2-3 5 2v4a2 2 0 0 1-2 2A18 18 0 0 1 2 4a2 2 0 0 1 2-2z"/></svg></div>
  <div>Phone:<br>0400 555 218</div>
</div>
<div class="abs contact-item" style="top:4800px">
  <div class="icon"><svg width="24" height="18" viewBox="0 0 24 18" fill="none" stroke="#111" stroke-width="2"><rect x="1" y="1" width="22" height="16" rx="2"/><path d="M1 2l11 9 11-9"/></svg></div>
  <div>Mail:<br>info@tamselloans.com.au</div>
</div>

<div class="abs copyright">© Copyright 2021 | All Rights Reserved Tamsel Loans . Privacy Policy</div>

</body>
</html>
```